we need an experienced designer to design the tube for our toothpaste

Design guidelines:
1. On the front side, our product logo (‘K7320’) should be prominent enough.
2. Our brand logo (‘trelvine’) could be small-size and it's just a trademark indeed.

Some information here for your reference:
1. The color of toothpaste cap is white.
2. We hope that the primary color in the design is blue.
3.‘F’ in ‘K7320’ stands for ‘trelvine’ and ‘fluoride’.
4. We will use aluminum-plastic composite materials to make toothpaste tubes. In addition to the design, we also hope that you can make relevant suggestions on the special requirements of printing.

At last, we hope that you could submit both 2D design and 3D visual effects.

Colors
0094D4
00A9DD
6FCCEA
C7EBF8
E9F6FB

Requirements
Must have
• as attached

```html
<!DOCTYPE html>
<html lang="en">
<head>
<meta charset="utf-8">
<title>K7320 Orthodontic Toothpaste – Tube Label</title>
<link href="https://fonts.googleapis.com/css2?family=Arimo:ital,wght@0,700;1,700&family=Barlow+Condensed:wght@400;500&display=swap" rel="stylesheet">
<style>
  :root {
    --stage: #aba5a3;
    --blue: #0094d4;
    --blue-mid: #00a9dd;
    --blue-soft: #6fccea;
    --blue-pale: #c7ebf8;
    --blue-mist: #e9f6fb;
    --white: #ffffff;
    --ink: #1c1c1c;
    --blush: #f6b4a4;
    --blush-light: #fbd3c8;
    --gum: #ec8a8f;
  }
  * { box-sizing: border-box; margin: 0; padding: 0; }
  html, body { width: 879px; height: 1200px; overflow: hidden; }
  body { background: var(--stage); position: relative; font-family: "Arimo", Arial, sans-serif; }

  .label {
    position: absolute; left: 20px; top: 346px;
    width: 840px; height: 508px;
    background: var(--white);
    overflow: hidden;
    border-left: 1px solid #333;
  }
  .label__hero-bg { position: absolute; left: 0; top: 0; }

  .brand {
    position: absolute; left: 38px; top: 118px;
    display: flex; align-items: center; gap: 6px;
    font-family: "Arimo", Arial, sans-serif; font-weight: 700;
    font-size: 30px; color: var(--blue); letter-spacing: -0.5px;
  }
  .brand__dot { width: 9px; height: 9px; border-radius: 50%; background: var(--blue); }
  .variant {
    position: absolute; left: 38px; top: 172px;
    font-weight: 700; font-size: 17px; line-height: 22px; color: var(--ink);
  }

  .eyebrow {
    position: absolute; left: 226px; top: 10px;
    font-style: italic; font-weight: 700; font-size: 24px; color: var(--white); letter-spacing: 0.3px;
  }
  .product-name {
    position: absolute; left: 224px; top: 34px;
    font-family: "Arimo", Arial, sans-serif; font-weight: 700;
    font-size: 128px; line-height: 1; color: var(--white); letter-spacing: -2px;
  }
  .paste-swirl {
    position: absolute; left: 248px; top: 156px; width: 192px; height: 48px;
    border-radius: 60% 40% 50% 50% / 60% 60% 40% 40%;
    background: linear-gradient(100deg, var(--blue) 0%, var(--blue-mist) 40%, var(--blue-soft) 75%, var(--white) 100%);
  }
  .strength-pill {
    position: absolute; left: 420px; top: 165px; width: 284px; height: 34px;
    border-radius: 8px;
    background: linear-gradient(90deg, var(--blush) 0%, var(--blush-light) 100%);
    font-style: italic; font-weight: 700; font-size: 22px; line-height: 34px;
    color: var(--ink); padding-left: 26px;
  }
  .claims {
    position: absolute; left: 228px; top: 212px;
    font-weight: 700; font-size: 15.5px; line-height: 22px; color: var(--white); letter-spacing: 0.2px;
  }

  .benefits {
    position: absolute; left: 29px; top: 266px; width: 259px; height: 242px;
    background: var(--blue); border-top-right-radius: 32px; color: var(--white);
  }
  .benefits__title {
    position: absolute; left: 16px; top: 14px;
    font-family: "Barlow Condensed", Arial, sans-serif; font-weight: 500;
    font-size: 18px; line-height: 22px; color: var(--blue-mist);
  }
  .benefits__art {
    position: absolute; top: 66px; height: 88px;
    border-radius: 40% 40% 50% 50%;
    background: linear-gradient(180deg, var(--blue-mist) 0%, var(--white) 45%, var(--gum) 100%);
  }
  .benefits__art--braces { left: 11px; width: 110px; }
  .benefits__art--aligners { left: 137px; width: 107px; }
  .benefits__list {
    position: absolute; left: 19px; top: 160px; list-style: none;
    font-weight: 700; font-size: 17px; line-height: 24.5px; color: var(--blue-mist);
  }
  .benefits__list li::before { content: "•"; margin-right: 12px; }

  .info {
    position: absolute; left: 302px; top: 290px; width: 485px;
    font-family: "Barlow Condensed", Arial, sans-serif; font-weight: 400;
    font-size: 18.5px; line-height: 24px; color: var(--ink);
  }
  .info p { margin-bottom: 11px; }
  .info__key { color: var(--blue); font-weight: 500; }
</style>
</head>
<body>
  <section class="label" aria-label="K7320 orthodontic toothpaste tube label, flat artwork">
    <svg class="label__hero-bg" width="840" height="264" viewBox="0 0 840 264" aria-hidden="true">
      <defs>
        <linearGradient id="heroBlue" x1="0" y1="0" x2="1" y2="0">
          <stop offset="0" stop-color="#0094d4"/>
          <stop offset="1" stop-color="#0a9de0"/>
        </linearGradient>
      </defs>
      <path d="M194 0 C150 60 148 200 236 264 L840 264 L840 0 Z" fill="url(#heroBlue)"/>
    </svg>

    <div class="brand"><span>trelvine</span><span class="brand__dot"></span></div>
    <div class="variant">Double Mint<br>NET WT. 85g</div>

    <div class="eyebrow">ORTHODONTIC TOOTHPASTE</div>
    <div class="product-name">K7320</div>
    <div class="paste-swirl" role="img" aria-label="Illustration of a blue and white toothpaste swirl"></div>
    <div class="strength-pill">Fluoride 1450 ppm</div>
    <div class="claims">
      ENHANCED CAVITY PREVENTION AND GUM PROTECTION<br>
      FOR USE WHEN WEARING METAL BRACES AND CLEAR ALIGNERS
    </div>

    <div class="benefits">
      <div class="benefits__title">PREMIUM ORAL CARE DURING<br>ORTHODONTIC TREATMENT</div>
      <div class="benefits__art benefits__art--braces" role="img" aria-label="Illustration of teeth with metal braces under a toothpaste swirl"></div>
      <div class="benefits__art benefits__art--aligners" role="img" aria-label="Illustration of teeth with clear aligners under a toothpaste swirl"></div>
      <ul class="benefits__list">
        <li>Prevent Cavity</li>
        <li>Freshen Breath</li>
        <li>Strengthen Teeth</li>
      </ul>
    </div>

    <div class="info">
      <p><span class="info__key">Directions:</span> Apply at least one inch strip of the product onto a soft bristle toothbrush. Brush teeth thoroughly, for at least three minutes twice a day.</p>
      <p><span class="info__key">Ingredients:</span> Aqua, Sorbitol, Hydrated Silica, Glycerin, PEG-12, Sodium Lauryl Sulfate, Aroma, Cellulose Gum, Titanium Dioxide, Potassium Sorbate, Allantoin, Sodium Fluoride, Citric Acid, Peppermint Essence, Sodium Saccharin, CI 47005, CI 42090, Cinnamal.</p>
      <p><span class="info__key">Warnings:</span> Do not ingest. Keep out of reach of children under 6 years of age.</p>
    </div>
  </section>
</body>
</html>
```